Break The Chain by Lena Varo

I am the Founder of a Not For Profit and writing a book about my story to raise funds for the work we do within our community.

It is my first book and would like a really cool cover, the title is:

BREAK THE CHAIN BEFORE IT BINDS YOU - How I Rebuilt a Life Through Cravings, Mania and Despair.

Author: Lena Varo

I plan to release the Quillo and Tunora copy on December 24, 2013 to commemorate the passing of my beloved Father in 2009 and this would make him very proud.

I need a book cover now so I can start marketing, here is Chapter List to give you a flavour:

Chapter One - Addiction Epidemic Worldwide

Chapter Two - Bipolar Kills

Chapter Three - Surviving Suicide

Chapter Four - Recovery Goals

Chapter Five – Healing Oneself

Chapter Six – Spirituality as the Key to Healing

Chapter Seven – Living a Life of Purpose

I have also uploaded current Best Sellers on Bookvale. I want the text to be: Purple and Yellow for BREAK THE CHAIN (My Charity colours). Please check out the website as well to get a feel for what I believe and stand for. The book pre-order is in the website too so I really need money to raise funds. Charity is Down to nothing at all! But as you can imagine the clients have addiction problems hence only efforts like book sales really guarantee or generate us any money as a Charity.

www.GuidanceOnRiverbend.Org.Au

I also want on the background to be Filipino flag components as that is where I was born. So red, blue, a big yellow sun and 3 yellow stars (attached flag to give you idea)

I have lots of pics so uploaded two that I think I want to use with cover.

Please please HELP!!!!!!

PS. The Velmora book is currently selling up to 300 - 500 copies daily and I did not particularly think it was a good cover therefore must be a good book.

Target Market(s)

20's - early 30's, disposable income, Asians, maybe living in US / Canada / Australia / Europe or travelled overseas with addiction issues / mental health issues.

Colors
ec2027
3276b5
6e489d
fbed23

Requirements
Must have
• Colours of the Philippines Flag as I am marketing to Filipinos predominantly, especially as that is where I am born.
Nice to have
• Bold Title like in Standing Tallish Book attached:

BREAK THE CHAIN BEFORE IT BINDS YOU

```html
<!DOCTYPE html>
<html lang="en">
<head>
<meta charset="utf-8">
<title>Break The Chain — Lena Varo</title>
<link href="https://fonts.googleapis.com/css2?family=Archivo+Black&family=Roboto:wght@300;400&display=swap" rel="stylesheet">
<style>
  :root {
    --stage: #f3f3f4;
    --paper: #ffffff;
    --band-grey: #e4e4e6;
    --tag-grey: #f2f2f3;
    --flag-red: #ec2027;
    --flag-blue: #3276b5;
    --charity-purple: #6e489d;
    --title-purple: #8e2a8f;
    --sun-yellow: #fbed23;
    --chapter-blue: #4a7dc0;
    --author-blue: #2f6fb0;
    --caption-grey: #9a9aa0;
  }
  * { margin: 0; padding: 0; box-sizing: border-box; }
  html, body {
    width: 1200px;
    height: 1000px;
    overflow: hidden;
    background: var(--stage);
  }
  .canvas {
    position: relative;
    width: 1200px;
    height: 1000px;
  }
  .book-cover {
    position: absolute;
    left: 314px;
    top: 94px;
    width: 572px;
    height: 812px;
    background: var(--paper);
    box-shadow: 0 0 0 1px #dcdcdf;
  }
  .book-cover svg { display: block; width: 100%; height: 100%; }
  .tagline {
    font-family: "Roboto", sans-serif;
    font-weight: 400;
    font-size: 11px;
    fill: var(--charity-purple);
  }
  .tagline-quote {
    font-family: "Roboto", sans-serif;
    font-size: 17px;
  }
  .title-top {
    font-family: "Archivo Black", sans-serif;
    font-size: 56px;
    fill: var(--title-purple);
  }
  .title-main {
    font-family: "Archivo Black", sans-serif;
    font-size: 90px;
    fill: var(--flag-red);
  }
  .title-sub {
    font-family: "Roboto", sans-serif;
    font-weight: 300;
    font-size: 19px;
    fill: var(--title-purple);
    letter-spacing: 0.3px;
  }
  .chapter-list {
    font-family: "Roboto", sans-serif;
    font-weight: 300;
    font-size: 10px;
    fill: var(--chapter-blue);
  }
  .author-name {
    font-family: "Roboto", sans-serif;
    font-weight: 400;
    font-size: 19px;
    fill: var(--author-blue);
  }
  .author-role {
    font-family: "Roboto", sans-serif;
    font-weight: 300;
    font-size: 11px;
    fill: var(--caption-grey);
  }
</style>
</head>
<body>
<main class="canvas">
  <article class="book-cover">
    <svg viewBox="0 0 520 738" xmlns="http://www.w3.org/2000/svg">
      <defs>
        <linearGradient id="portrait-tone" x1="0" y1="0" x2="1" y2="1">
          <stop offset="0" stop-color="#6d6d6f"/>
          <stop offset="0.5" stop-color="#bdbdbf"/>
          <stop offset="1" stop-color="#8a8a8c"/>
        </linearGradient>
      </defs>

      <g class="header-band">
        <polygon points="0,0 520,0 520,70 0,92" fill="var(--band-grey)"/>
        <polygon class="tagline-tag" points="110,31 515,23 515,83 118,103" fill="var(--tag-grey)"/>
        <g transform="rotate(-1.6 130 66)">
          <text class="tagline" x="124" y="68"><tspan class="tagline-quote" dy="-3">“</tspan><tspan dy="3"> HOW I REBUILT A LIFE THROUGH CRAVINGS, MANIA AND DESPAIR.</tspan><tspan class="tagline-quote" dy="-3">”</tspan></text>
        </g>
      </g>

      <polygon class="portrait" role="img" aria-label="Black and white portrait photograph of the author"
               points="18,105 260,243 18,408" fill="url(#portrait-tone)"/>

      <g class="title-block" transform="translate(40 458) rotate(-32)">
        <text class="title-top" x="0" y="0">BREAK THE</text>
        <text class="title-main" x="8" y="82">CHAIN</text>

        <g class="flag-squares">
          <rect x="412" y="-46" width="32" height="32" fill="var(--flag-red)"/>
          <rect x="412" y="-6" width="32" height="32" fill="var(--flag-blue)"/>
          <rect x="412" y="34" width="32" height="32" fill="var(--charity-purple)"/>
          <rect x="412" y="74" width="32" height="32" fill="var(--sun-yellow)"/>
        </g>

        <rect class="sun-band" x="-6" y="94" width="192" height="28" fill="var(--sun-yellow)"/>
        <polygon class="purple-wedge" points="-7,125 185,128 166,281" fill="var(--title-purple)"/>

        <text class="title-sub" x="196" y="114">BEFORE IT BINDS YOU</text>

        <g class="chapter-list">
          <text x="192" y="140">Chapter One - Addiction Epidemic Worldwide</text>
          <text x="192" y="158">Chapter Two - Bipolar Kills</text>
          <text x="192" y="176">Chapter Three - Surviving Suicide</text>
          <text x="192" y="194">Chapter Four - Recovery Goals</text>
          <text x="192" y="212">Chapter Five – Healing Oneself</text>
          <text x="192" y="230">Chapter Six – Spirituality as the Key to Healing</text>
          <text x="192" y="248">Chapter Seven – Living a Life of Purpose</text>
        </g>
      </g>

      <g class="footer-band">
        <polygon points="0,660 520,640 520,738 0,738" fill="var(--band-grey)"/>
        <polygon class="author-tag" points="350,663 520,652 520,720 354,726" fill="var(--tag-grey)"/>
        <text class="author-name" x="380" y="697">Lena Varo</text>
        <text class="author-role" x="441" y="711">Author</text>
      </g>
    </svg>
  </article>
</main>
</body>
</html>
```